Brinewardsea.com Website design needed!!

We are looking for a website layout to match the attached logo. We specialize in Dive Charters and currently are located in the Virgin Islands off of St. Thomas. Please create a design that is compatible with Bootstrap and have the grid in mind. WE are looking for creative and extremely professional layout design.

Target Market(s)

Scuba Diving, Divers looking for a diving charter in the Virgin Islands.

Number of Pages Required

3 page

Font styles to use
Serif

Requirements
Must have
• Must be Bootstrap friendly.
• Must work with the logo we provided. Colors etc.

```html
<!DOCTYPE html>
<html lang="en">
<head>
<meta charset="utf-8">
<title>Brinewardsea — Dive Charters St. Thomas</title>
<link href="https://fonts.googleapis.com/css2?family=Dancing+Script:wght@600;700&family=Open+Sans:wght@400;600;700&display=swap" rel="stylesheet">
<style>
:root{
  --navy:#2a2160;
  --ocean:#1a8fd0;
  --ocean-deep:#0b3f78;
  --red:#d8232a;
  --ink:#333;
  --muted:#555;
  --sand:#e8e3de;
  --cloud:#ececec;
  --charcoal:#444;
  --teal-dark:#0f3b3c;
  --white:#fff;
}
*{box-sizing:border-box;margin:0;padding:0}
html,body{width:682px;height:1200px;overflow:hidden}
body{position:relative;font-family:"Open Sans",Arial,sans-serif;color:var(--ink);background:var(--white)}
.abs{position:absolute}
.script{font-family:"Dancing Script",cursive;font-weight:700}
.script .accent{color:var(--red)}
.section-title{position:absolute;left:0;width:682px;text-align:center;font-size:20px;color:var(--navy)}

/* header */
.topbar{left:0;top:0;width:682px;height:32px;background:var(--charcoal)}
.band-left{left:0;top:32px;width:237px;height:72px;background:var(--navy)}
.band-right{left:237px;top:32px;width:445px;height:72px;background:var(--ocean)}
.header-box{left:56px;top:0;width:570px;height:80px;background:var(--white);border-top:2px solid var(--ocean)}
.brand{position:absolute;left:20px;top:16px;display:flex;align-items:center;gap:6px}
.brand-mark{width:18px;height:18px;border-radius:50%;background:var(--ocean)}
.brand-name{font-size:16px;font-weight:700;color:var(--red)}
.brand-sub{position:absolute;left:48px;top:40px;font-size:8px;font-weight:700;letter-spacing:1.5px;color:var(--navy)}
.nav{position:absolute;right:22px;top:30px;display:flex;gap:22px;align-items:center;font-family:"Dancing Script",cursive;font-size:9px;font-weight:600;color:var(--ocean)}
.nav .first{color:var(--navy)}
.call{right:56px;top:86px;display:flex;align-items:center;gap:8px;color:var(--white);font-size:7px}
.call-icon{width:15px;height:15px;border:1px solid var(--white);border-radius:50%;display:flex;align-items:center;justify-content:center}

/* hero */
.hero{left:0;top:104px;width:682px;height:305px;background:linear-gradient(160deg,#1f8fd6 0%,#1565b0 45%,#0b3a78 100%)}
.hero-title{left:56px;top:200px;color:var(--white);font-weight:700;font-size:17px;line-height:26px;letter-spacing:.3px}
.hero-arrow{top:230px}
.search{left:438px;top:142px;width:188px;height:230px;background:#0a2240;border:3px solid var(--ocean)}
.search-head{height:50px;background:var(--ocean);color:var(--white);text-align:center;padding-top:12px;font-size:9px;line-height:15px}
.search-head strong{font-size:12px;font-weight:700}
.search-opts{display:flex;justify-content:space-between;padding:16px 14px 0 14px;font-size:6.5px;color:var(--white)}
.search-opts span::before{content:"";display:inline-block;width:4px;height:4px;border-radius:50%;background:var(--white);margin-right:6px;vertical-align:middle}
.field{margin:10px 14px 0;height:27px;border:1px solid #7f8c99;color:var(--white);font-size:7px;padding:9px 6px}
.search .btn{margin:16px auto 0;display:block;width:66px}
.btn{height:25px;background:var(--ocean);color:var(--white);font-size:7px;font-weight:600;text-align:center;line-height:25px;border-bottom:2px solid #0f6fa8}

/* welcome */
.welcome-text{left:100px;top:454px;width:482px;text-align:center;font-size:6.8px;line-height:12.5px;color:var(--muted)}
.welcome-btn{left:315px;top:502px;width:51px}

/* services */
.services{left:0;top:550px;width:682px;height:224px;background:var(--sand)}
.service{top:590px;width:183px;height:151px;display:flex;align-items:center;justify-content:center}
.service-label{color:var(--white);font-size:10px;padding:9px 0;width:90px;text-align:center;border-top:1px solid var(--white);border-bottom:1px solid var(--white)}
.dot{top:754px;width:5px;height:5px}

/* holiday */
.holiday-panel{left:0;top:774px}
.holiday-copy{left:56px;top:868px;width:135px;color:var(--white)}
.holiday-copy h3{font-size:10px;font-weight:600;margin-bottom:8px}
.holiday-copy p{font-size:6.5px;line-height:12.5px}
.trip{top:838px;width:171px}
.trip-photo{height:119px}
.trip h4{margin-top:13px;font-size:10px;font-weight:600;color:var(--ocean)}
.trip p{margin-top:8px;font-size:6.5px;line-height:12.5px;color:var(--ink);text-align:justify}

/* clients */
.clients{left:0;top:1042px;width:682px;height:124px;background:var(--cloud)}
.client{top:1094px;width:83px;height:42px;background:var(--white);border:1px solid #d6d6d6;display:flex;align-items:center;justify-content:center;font-size:8px;font-weight:600;color:#6a6a6a}
.client-arrow{top:1104px}

/* footer */
.footer{left:0;top:1166px;width:682px;height:34px;background:var(--charcoal);color:var(--white);font-size:6.5px}
.footer .copy{position:absolute;left:56px;top:13px}
.social{position:absolute;right:30px;top:11px;display:flex;align-items:center;gap:6px;font-size:7px}
.social-item{display:flex;align-items:center;gap:3px;font-size:6px}
.social-item i{display:inline-block;width:8px;height:8px;background:var(--white)}
</style>
</head>
<body>

<!-- header -->
<div class="abs topbar"></div>
<div class="abs band-left"></div>
<div class="abs band-right"></div>
<header class="abs header-box">
  <div class="brand"><span class="brand-mark"></span><span class="brand-name">Brinewardsea</span></div>
  <div class="brand-sub">ST. THOMAS</div>
  <nav class="nav">
    <span class="first">Brinewardsea</span><span>About Us</span><span>Contact</span><span>Learn More</span><span>Schedule</span><span>Contacts</span>
    <svg width="8" height="8" viewBox="0 0 10 10"><circle cx="4" cy="4" r="3" fill="none" stroke="#222" stroke-width="1.6"/><line x1="6.2" y1="6.2" x2="9" y2="9" stroke="#222" stroke-width="1.8"/></svg>
  </nav>
</header>
<div class="abs call">
  <span class="call-icon"><svg width="7" height="7" viewBox="0 0 10 10"><path d="M2 1l2 2-1 1.5c.6 1.2 1.4 2 2.5 2.5L7 6l2 2-1.2 1.5C4.5 9 1 5.5.5 2.2z" fill="#fff"/></svg></span>
  Call Us +44 100 200 300
</div>

<!-- hero -->
<section class="abs hero" role="img" aria-label="Underwater photo of a scuba diver with yellow fins in clear blue water"></section>
<svg class="abs hero-arrow" style="left:24px" width="8" height="50" viewBox="0 0 8 50"><polyline points="7,0 1,25 7,50" fill="none" stroke="rgba(255,255,255,.5)" stroke-width="1"/></svg>
<svg class="abs hero-arrow" style="left:648px" width="8" height="50" viewBox="0 0 8 50"><polyline points="1,0 7,25 1,50" fill="none" stroke="rgba(255,255,255,.5)" stroke-width="1"/></svg>
<h1 class="abs hero-title">BRINEWARDSEA<br>CHARTERS AND SCUBA</h1>
<form class="abs search">
  <div class="search-head">Search for your dream charter<br><strong>TODAY!</strong></div>
  <div class="search-opts"><span>I have approximate dates</span><span>I'm flexible</span></div>
  <div class="field">First Name</div>
  <div class="field">Email</div>
  <div class="btn">FIND CHARTERS</div>
</form>

<!-- welcome -->
<h2 class="section-title script" style="top:426px">Welcome to <span class="accent">Brinewardsea</span></h2>
<p class="abs welcome-text">Lorem ipsum dolor sit amet, consectetur adipiscing elit. Fusce semper vitae leo sit amet vehicula. Sed viverra, justo ac consectetur hendrerit, lacus elit tempor urna, gravida mattis lacus ex sed sem. Nam consectetur, arcu in iaculis dapibus, urna felis congue elit, in consectetur nisi massa sed metus. Nullam a tortor ut mauris auctor interdum id vel neque. In commodo diam at faucibus dictum. Nulla condimentum elit a odio consectetur.</p>
<div class="abs btn welcome-btn">View info</div>

<!-- services -->
<section class="abs services" role="img" aria-label="Background photo of white sand with seashells"></section>
<h2 class="section-title script" style="top:558px">Water Services <span class="accent">We Offer</span></h2>
<div class="abs service" style="left:56px;background:linear-gradient(160deg,#1f6f86,#0b3444)" role="img" aria-label="Photo of a scuba diver near a reef"><span class="service-label">Scuba Diving</span></div>
<div class="abs service" style="left:249px;background:linear-gradient(180deg,#3f86b8,#164d80)" role="img" aria-label="Photo of a snorkeler swimming underwater"><span class="service-label">Snorkeling</span></div>
<div class="abs service" style="left:442px;background:linear-gradient(180deg,#6ea6d2,#1c5d8e)" role="img" aria-label="Photo of a kite surfer on the waves"><span class="service-label">Kite Surf</span></div>
<div class="abs dot" style="left:333px;background:var(--ocean)"></div>
<div class="abs dot" style="left:343px;background:#888"></div>

<!-- holiday trips -->
<svg class="abs holiday-panel" width="246" height="268" viewBox="0 0 246 268" role="img" aria-label="Underwater photo of a diver holding a camera"><defs><linearGradient id="deep" x1="0" y1="0" x2="0" y2="1"><stop offset="0" stop-color="#1f5a4e"/><stop offset="1" stop-color="#0b2f33"/></linearGradient></defs><polygon points="0,0 246,0 176,268 0,268" fill="url(#deep)"/></svg>
<div class="abs holiday-copy">
  <h3>Caribbean Luxury Yacht Charter</h3>
  <p>Lorem Ipsum is simply dummy text of the printing and typesetting industry. Lorem Ipsum has been the industry's standard dummy text...</p>
</div>
<h2 class="abs script" style="left:256px;top:802px;font-size:20px;color:var(--navy)">Holiday <span style="color:var(--red)">Trips</span></h2>
<article class="abs trip" style="left:255px">
  <div class="trip-photo" style="background:linear-gradient(160deg,#2a8fd0,#0d3f6e)" role="img" aria-label="Photo of a diver in a mask underwater"></div>
  <h4>Caribbean Luxury Yacht Charter</h4>
  <p>Lorem Ipsum is simply dummy text of the printing and typesetting industry. Lorem Ipsum has been the industry's standard dummy text...</p>
</article>
<article class="abs trip" style="left:445px">
  <div class="trip-photo" style="background:linear-gradient(180deg,#b9d7ee,#2a6aa8)" role="img" aria-label="Photo of a group of friends on a sailing yacht"></div>
  <h4>Caribbean Luxury Yacht Charter</h4>
  <p>Lorem Ipsum is simply dummy text of the printing and typesetting industry. Lorem Ipsum has been the industry's standard dummy text...</p>
</article>

<!-- clients -->
<section class="abs clients"></section>
<h2 class="section-title script" style="top:1062px">Our Valuable <span class="accent">Clients</span></h2>
<svg class="abs client-arrow" style="left:24px" width="8" height="20" viewBox="0 0 8 20"><polyline points="7,2 1,10 7,18" fill="none" stroke="#aaa" stroke-width="1.5"/></svg>
<div class="abs client" style="left:56px">Coralbay</div>
<div class="abs client" style="left:154px">Saltmere</div>
<div class="abs client" style="left:251px">Keelhart</div>
<div class="abs client" style="left:349px">Pelagion</div>
<div class="abs client" style="left:446px">Driftwell</div>
<div class="abs client" style="left:543px">Nautaro</div>
<svg class="abs client-arrow" style="left:650px" width="8" height="20" viewBox="0 0 8 20"><polyline points="1,2 7,10 1,18" fill="none" stroke="#aaa" stroke-width="1.5"/></svg>

<!-- footer -->
<footer class="abs footer">
  <span class="copy">© 2016 Brinewardsea All right reserved Term of Use</span>
  <div class="social">Follow us on :
    <span class="social-item"><i></i>Wavebook</span>
    <span class="social-item"><i></i>Chirpline</span>
    <span class="social-item"><i></i>Plusreef</span>
    <span class="social-item"><i></i>Linkharbor</span>
  </div>
</footer>

</body>
</html>
```